Corvane Solutions Website

Corvane Solutions (CS) provide Analytics & Enterprise Performance Management (EPM) advisory & consultancy services. We are passionate about data and making a difference for our clients by working in partnership with them, helping them on their journey to becoming an Corvane Solution. We deliver insights which give our clients a competitive edge and a much deeper understanding of their organisation.

We need a website which shows who we are, what we do and how we do it.

www.corvane-solutions.com is our very basic website at the moment. We want to completely revamp it with a corporate look

```html
<!DOCTYPE html>
<html lang="en">
<head>
<meta charset="utf-8">
<title>Corvane Solutions</title>
<link href="https://fonts.googleapis.com/css2?family=Montserrat:wght@300;400;500;600;700;800&display=swap" rel="stylesheet">
<style>
:root{
  --navy:#0e3150;
  --ink:#1b1b1b;
  --orange:#f48c1c;
  --peach:#fdebdc;
  --card:#fafafa;
  --band:#f0f0f0;
  --hero-top:#0d1322;
  --hero-bottom:#05304a;
  --icon-fill:#dfe5ea;
  --red:#e0262c;
}
*{margin:0;padding:0;box-sizing:border-box}
html,body{width:1200px;height:2244px;overflow:hidden;background:#fff;font-family:'Montserrat',sans-serif;color:var(--ink)}
.page{position:relative;width:1200px;height:2244px}
.brand{position:absolute;display:flex;align-items:center;gap:8px;color:var(--navy);font-weight:700;font-size:13px;line-height:14px;letter-spacing:.3px}
.brand-mark{width:34px;height:34px;border-radius:50%;border:5px solid var(--navy)}
.site-header .brand{left:135px;top:17px}
.main-nav{position:absolute;top:31px;left:0;width:1200px;font-size:13px;color:var(--navy);font-weight:500;letter-spacing:.3px}
.main-nav span{position:absolute}
.hero{position:absolute;left:0;top:77px;width:1200px;height:560px;background:linear-gradient(160deg,var(--hero-top) 0%,#0b2236 50%,var(--hero-bottom) 100%);overflow:hidden}
.hero-photo{position:absolute;left:600px;top:12px;width:600px;height:548px;border-radius:300px 0 0 0;border-bottom-right-radius:230px;background:radial-gradient(circle at 60% 45%,#e48a22 0%,#7a5a3a 30%,#2a4a5a 60%,#1a3450 100%)}
.hero-title{position:absolute;left:139px;top:130px;color:#fff;font-weight:800;font-size:47px;line-height:52px}
.hero-text{position:absolute;left:139px;top:297px;width:480px;color:#fff;font-size:16.5px;line-height:20px;font-weight:400}
.btn{position:absolute;display:flex;align-items:center;justify-content:center;background:var(--orange);border-radius:24px;font-weight:700;font-size:13px;letter-spacing:.3px}
.hero .btn{left:139px;top:381px;width:236px;height:44px;color:#fff}
.welcome-kicker{position:absolute;top:741px;width:1200px;text-align:center;color:var(--orange);font-size:14px;font-weight:500}
.welcome-title{position:absolute;top:768px;width:1200px;text-align:center;font-size:21px;font-weight:700;letter-spacing:.3px}
.service{position:absolute;top:891px;width:249px;height:233px;background:var(--card);border-radius:8px;text-align:center}
.service.is-active{background:var(--peach)}
.service.is-active::after{content:"";position:absolute;left:0;bottom:-3px;width:249px;height:4px;background:var(--orange);border-radius:2px}
.service-icon{position:absolute;left:89px;top:24px;width:72px;height:72px;border-radius:8px;background:var(--icon-fill)}
.service h3{position:absolute;top:117px;width:100%;color:var(--navy);font-size:19.5px;font-weight:500}
.service p{position:absolute;top:151px;left:20px;width:209px;font-size:12.5px;line-height:20px;color:#333}
.partner-badge{position:absolute;left:1030px;top:1254px;width:104px;height:24px;background:var(--red);border-radius:2px}
.question-band{position:absolute;left:48px;top:1326px;width:1104px;height:419px;background:var(--band)}
.question-photo{position:absolute;left:9px;top:1296px;width:561px;height:449px;background:linear-gradient(90deg,#a9a9a9 0%,#5a4e48 45%,#2b2b35 75%,#6f6f6f 100%);border-radius:180px 180px 0 0}
.question-title{position:absolute;right:118px;top:1455px;font-size:44px;font-weight:800}
.question-text{position:absolute;right:118px;top:1538px;width:460px;text-align:right;font-size:16.5px;line-height:20px;font-weight:300;color:#333}
.question-band ~ .btn{left:888px;top:1624px;width:194px;height:43px;color:var(--ink)}
.site-footer .brand{left:505px;top:1874px}
.footer-nav{position:absolute;top:1975px;left:0;width:1200px;font-size:11px;color:#333;letter-spacing:.3px}
.footer-nav span{position:absolute}
.social{position:absolute;top:2030px;width:43px;height:26px;border-radius:13px;background:#ececec}
.contact-line{position:absolute;width:1200px;text-align:center;font-size:10px;color:#666;font-weight:300}
.to-top{position:absolute;left:1128px;top:2130px}
.divider{position:absolute;left:0;top:2191px;width:1200px;height:1px;background:#e4e4e4}
.copyright{position:absolute;top:2214px;width:1200px;text-align:center;font-size:7px;color:#888}
</style>
</head>
<body>
<div class="page">
  <header class="site-header">
    <div class="brand"><span class="brand-mark"></span><span>CORVANE<br>SOLUTIONS</span></div>
    <nav class="main-nav">
      <span style="left:649px">Our Services</span>
      <span style="left:786px">Case Studies</span>
      <span style="left:924px">About Us</span>
      <span style="left:1047px">Contact Us</span>
    </nav>
  </header>

  <section class="hero">
    <div class="hero-photo" role="img" aria-label="Photo of two business colleagues reviewing a folder, one on the phone"></div>
    <h1 class="hero-title">Cutting Edge<br>Business Intelligence<br>Services</h1>
    <p class="hero-text">implementation and support of Business Intelligence, EPM and Data Analytics business solutions, both in the Cloud and on-premise.</p>
    <a class="btn">Our Business Solutions</a>
  </section>

  <p class="welcome-kicker">WELCOME TO</p>
  <h2 class="welcome-title">CORVANE SOLUTIONS</h2>

  <article class="service is-active" style="left:154px">
    <div class="service-icon" role="img" aria-label="Line illustration for advisory and architecture"></div>
    <h3>Advise &amp; Architect</h3>
    <p>Outlived no dwelling denoting in peculiar as he believed.</p>
  </article>
  <article class="service" style="left:476px">
    <div class="service-icon" role="img" aria-label="Line illustration for design and implementation"></div>
    <h3>Design &amp; Implement</h3>
    <p>Outlived no dwelling denoting in peculiar as he believed.</p>
  </article>
  <article class="service" style="left:797px">
    <div class="service-icon" role="img" aria-label="Line illustration for optimisation and management"></div>
    <h3>Optimse &amp; Manage</h3>
    <p>Outlived no dwelling denoting in peculiar as he believed.</p>
  </article>

  <div class="partner-badge" role="img" aria-label="Technology partner badge"></div>

  <section>
    <div class="question-band"></div>
    <div class="question-photo" role="img" aria-label="Photo of two smiling colleagues with arms crossed"></div>
    <h2 class="question-title">Have a Question?</h2>
    <p class="question-text">implementation and support of Business Intelligence, EPM and Data Analytics business solutions, both in the Cloud and on-premise.</p>
    <a class="btn">Contact Us</a>
  </section>

  <footer class="site-footer">
    <div class="brand"><span class="brand-mark"></span><span>CORVANE<br>SOLUTIONS</span></div>
    <nav class="footer-nav">
      <span style="left:323px">Home</span>
      <span style="left:415px">Our Services</span>
      <span style="left:537px">Case Studies</span>
      <span style="left:660px">About Us</span>
      <span style="left:767px">Contact Us</span>
    </nav>
    <span class="social" style="left:496px"></span>
    <span class="social" style="left:544px"></span>
    <span class="social" style="left:594px"></span>
    <span class="social" style="left:645px"></span>
    <p class="contact-line" style="top:2088px"><svg width="9" height="11" viewBox="0 0 9 11"><path d="M4.5 0A4 4 0 0 0 .5 4C.5 7 4.5 11 4.5 11S8.5 7 8.5 4A4 4 0 0 0 4.5 0Z" fill="#ccc"/></svg> 14 Harwell Quay, Linden Row, Dublin 4, D04 KR21</p>
    <p class="contact-line" style="top:2105px">info@corvane-solutions.com</p>
    <svg class="to-top" width="20" height="22" viewBox="0 0 20 22" fill="none" stroke="#0e3150" stroke-width="2.5" stroke-linecap="round"><path d="M2 2H18M10 21V8M4 13L10 7L16 13"/></svg>
    <div class="divider"></div>
    <p class="copyright">Copyright © 2022 Corvane Solutions. Use of this website constitutes acceptance of our User Agreement and Privacy Policy.</p>
  </footer>
</div>
</body>
</html>
```